Business Card Design Project

I am community manager and social media strategist. I need a double sided business card with company logo and name. Looking for something professional, elegant but also a little bit original.

• - The logo and the colours are the company colours and a required to stay.
- The size should be: 84 x 55 mm (or 3.30 x 2.16)
- The file size should be: 1039 x 697 pixels (300 dpi)
- I'd like rounded corners. :)

Use the following contact information for the card:

Léonie Vardin
Stratégie médias sociaux / community management / édition de sites sociaux
mob. : 0687529103
leonie.vardin@postelune.fr
Twitter. : @lvardin
Skype : vardin.leonie

```html
<!DOCTYPE html>
<html lang="fr">
<head>
<meta charset="utf-8">
<title>MERIVA – cartes de visite</title>
<link rel="stylesheet" href="https://fonts.googleapis.com/css2?family=Alegreya:wght@400;700&display=swap">
<style>
  :root {
    --page: #ffffff;
    --card: #ffffff;
    --card-edge: #d6d6d6;
    --brand-blue: #1b75bb;
    --brand-deep: #0d5186;
    --brand-mid: #1f6ba6;
    --ink: #3a3a3a;
    --ink-soft: #8a8a8a;
    --faint: #eeeeee;
  }
  * { margin: 0; padding: 0; box-sizing: border-box; }
  html, body { width: 1200px; height: 900px; overflow: hidden; background: var(--page); }
  body { position: relative; font-family: "Alegreya", Georgia, serif; color: var(--ink); }

  .card {
    position: absolute;
    width: 278px; height: 182px;
    background: var(--card);
    border: 1px solid var(--card-edge);
    overflow: hidden;
  }
  .card-number {
    position: absolute;
    font-size: 8px; color: var(--ink-soft);
  }

  /* recto */
  .card-front {
    left: 490px; top: 134px; width: 279px; height: 183px;
    border: none;
    background: linear-gradient(120deg, var(--brand-mid) 0%, var(--brand-deep) 70%);
  }
  .front-mark {
    position: absolute; left: 0; right: 0; top: 44px;
    display: flex; flex-direction: column; align-items: center; gap: 8px;
  }
  .front-mark .dot { width: 40px; height: 40px; border-radius: 50%; background: #fff; }
  .front-mark .brand-name { color: #fff; font-weight: 700; font-size: 27px; letter-spacing: 1px; }
  .front-band {
    position: absolute; left: 0; right: 0; bottom: 0; height: 36px;
    background: linear-gradient(to top, rgba(255,255,255,0.28), rgba(255,255,255,0.05));
  }

  /* verso contact block */
  .contact { position: absolute; }
  .contact .name { color: var(--brand-blue); font-size: 13.5px; line-height: 15px; }
  .contact .role { font-size: 9.5px; line-height: 12px; margin-top: 2px; }
  .contact dl {
    display: grid; margin-top: 10px;
    font-size: 9.5px; line-height: 12.5px;
  }
  .contact dt, .contact dd { white-space: nowrap; }
  .contact .email { color: var(--brand-blue); }
  .contact.soft .muted { color: var(--ink-soft); }

  .brand-small { position: absolute; display: flex; align-items: center; gap: 5px; }
  .brand-small .dot { border-radius: 50%; background: var(--brand-blue); }
  .brand-small .brand-name { color: var(--brand-blue); font-weight: 700; }

  .faint-name {
    position: absolute; right: -30px; bottom: 10px;
    font-size: 46px; font-weight: 700; color: var(--faint);
  }
  .big-circle {
    position: absolute; left: -64px; top: 36px;
    width: 120px; height: 120px; border-radius: 50%; background: var(--brand-blue);
  }
  .side-name {
    position: absolute; left: 6px; top: 160px;
    font-size: 10px; font-weight: 700; color: var(--brand-blue);
  }
</style>
</head>
<body>

  <section class="card card-front" aria-label="Recto">
    <div class="front-mark">
      <span class="dot"></span>
      <span class="brand-name">MERIVA</span>
    </div>
    <div class="front-band" role="img" aria-label="Frise de pictogrammes des réseaux sociaux en bleu clair"></div>
  </section>

  <!-- Verso 1 -->
  <section class="card" style="left:267px; top:361px;">
    <div class="contact" style="left:22px; top:57px;">
      <p class="name">Léonie Vardin</p>
      <p class="role">Stratégie médias sociaux / community management<br>/ édition de sites sociaux</p>
      <dl style="grid-template-columns:42px auto;">
        <dt class="email">Email</dt><dd class="email">: leonie.vardin@postelune.fr</dd>
        <dt>Mobile</dt><dd>: 0687529103</dd>
        <dt>Twitter</dt><dd>: @lvardin</dd>
        <dt>Skype</dt><dd>: vardin.leonie</dd>
      </dl>
    </div>
  </section>
  <span class="card-number" style="left:538px; top:548px;">1</span>

  <!-- Verso 2 -->
  <section class="card" style="left:628px; top:361px;">
    <span class="faint-name" aria-hidden="true">MERIVA</span>
    <div class="brand-small" style="right:10px; top:14px;">
      <span class="brand-name" style="font-size:10px;">MERIVA</span>
      <span class="dot" style="width:20px; height:20px;"></span>
    </div>
    <div class="contact" style="left:21px; top:58px;">
      <p class="name">Léonie Vardin</p>
      <p class="role">Stratégie médias sociaux / community management<br>/ édition de sites sociaux</p>
      <dl style="grid-template-columns:85px auto;">
        <dt class="email">Email</dt><dd class="email">: leonie.vardin@postelune.fr</dd>
        <dt>Mobile</dt><dd>: 0687529103</dd>
        <dt>Twitter</dt><dd>: @lvardin</dd>
        <dt>Skype</dt><dd>: vardin.leonie</dd>
      </dl>
    </div>
  </section>
  <span class="card-number" style="left:900px; top:548px;">2</span>

  <!-- Verso 3 -->
  <section class="card" style="left:267px; top:572px;">
    <div class="brand-small" style="right:22px; top:23px;">
      <span class="dot" style="width:26px; height:26px;"></span>
      <span class="brand-name" style="font-size:18px;">MERIVA</span>
    </div>
    <div class="contact soft" style="left:18px; top:65px;">
      <p class="name">Léonie Vardin</p>
      <p class="role">Stratégie médias sociaux / community management /<br>édition de sites sociaux</p>
      <dl style="grid-template-columns:42px auto; margin-left:20px;">
        <dt class="email">Email</dt><dd class="email">: leonie.vardin@postelune.fr</dd>
        <dt class="muted">Mobile</dt><dd class="muted">: 0687529103</dd>
        <dt class="muted">Twitter</dt><dd class="muted">: @lvardin</dd>
        <dt class="muted">Skype</dt><dd class="muted">: vardin.leonie</dd>
      </dl>
    </div>
  </section>
  <span class="card-number" style="left:538px; top:759px;">3</span>

  <!-- Verso 4 -->
  <section class="card" style="left:628px; top:570px;">
    <span class="big-circle" aria-hidden="true"></span>
    <span class="side-name">MERIVA</span>
    <div class="contact" style="left:83px; top:38px;">
      <p class="name">Léonie Vardin</p>
      <p class="role">Stratégie médias sociaux / community<br>management / édition de sites sociaux</p>
      <dl style="grid-template-columns:42px auto;">
        <dt class="email">Email</dt><dd class="email">: leonie.vardin@postelune.fr</dd>
        <dt>Mobile</dt><dd>: 0687529103</dd>
        <dt>Twitter</dt><dd>: @lvardin</dd>
        <dt>Skype</dt><dd>: vardin.leonie</dd>
      </dl>
    </div>
  </section>
  <span class="card-number" style="left:900px; top:759px;">4</span>

</body>
</html>
```